Venture Capital firm needs modern business cards

We are a Venture Capital firm within financial services/Asset management. The industry generally has basic business cards with black, blue and maybe green/yellow design elements.
Our firm has a four-colour swoosh logo. We are based in London and want to stand out, just a little bit!, from the crowd. Our company is called ROLK Investments and the 'C' stands for collaboration thus using artfolkhub is a natural portal for our business card design competition. Our logo came via artfolkhub too!
We use 'Venture Partner in Asset Management' as our tagline and this is Trademark registered. We operate in a conservative industry and we should not overstep our mark. The logo is colorful as it is and therefore the rest of the design should not be too fanciful.
The objective is twofold: make our logo element stick and memorable with our audience, whilst representing a conservative yet young image.
The Business Card obviously needs a field for Name, Surname, Job Title, Adress fields: Street, City, Postcode, Country, telefone and cell number, website address, etc.
We have uploaded the ai file. We trust that these are OK. If not, please advise.
Reason: We have have been busy with a client engagement. We will set the project as Guaranteed in return for the troubles we cause. Apologies for the confusion.
Thank you all for these great and creative design suggestions. The team is very happy with a number of your ideas! We will be in touch tomorrow to give individual feedback before the project closes on Friday. We look forward to working with some of you to narrow down your creations. Thank you, ROLK Investments team.
All,
Target Market(s)
Financial Services Professionals, Investors, Media, 35-70 years, mainly male, well educated
Industry/Entity Type
Conservative
Requirements
Must have
- We must make use of our logo and potential tagline 'Venture Partner in Asset Management' as we are establishing a new Brand and new company in the market.
We can use 'ROLK', 'ROLK Investments', and 'ROLK Investments'+tagline 'Venture Partner in Asset Management' or simply the four-colour swoosh plus the name of the company as part of the text. (see files)
All design elements are available in black or grey-scale if required. (grey scale swoosh attached).
Due to regulation we must have the following wording on the card in small print 'ROLK Investments is an Appointed Representative of Brambury Monetary Ventures Limited, which is authorised by the Pemberton Oversight Board'.
Nice to have
- We would consider designs that make use of different printing techniques such embossing/debossing, UV spot etc.
We attach our colour palette in the files section for your reference.
Should not have
- The font we use for our company name is 'EXO' so do not use a font style that clashes with the corporate fonts, please.
Do not use other design elements than the ones we provide in the file library as part of this project.

```html
<!DOCTYPE html>
<html lang="en">
<head>
<meta charset="utf-8">
<title>ROLK Investments – Business Cards</title>
<link rel="stylesheet" href="https://fonts.googleapis.com/css2?family=Exo:wght@400;500&family=PT+Sans:ital,wght@0,400;1,400&display=swap">
<style>
  :root {
    --backdrop: #262626;
    --card-white: #f7f7f7;
    --card-charcoal: #3b3b3c;
    --ink: #4a4a4c;
    --ink-soft: #6a6a6c;
    --deboss: #323233;
    --brand-grey: #4d4d4f;
  }
  * { margin: 0; padding: 0; box-sizing: border-box; }
  html, body {
    width: 1200px; height: 900px; overflow: hidden;
    background: var(--backdrop);
  }
  .stage {
    position: relative; width: 1200px; height: 900px;
  }
  .card {
    position: absolute; width: 560px; height: 320px;
    border-radius: 3px;
  }
  .card--front {
    left: 320px; top: 100px;
    background: var(--card-white);
    color: var(--ink);
    font-family: "PT Sans", Arial, sans-serif;
  }
  .card--back {
    left: 320px; top: 480px;
    background: var(--card-charcoal);
  }

  /* front card */
  .contact { position: absolute; left: 44px; top: 58px; }
  .contact__name { font-size: 19px; letter-spacing: 0.2px; }
  .contact__title { font-size: 13px; color: var(--ink-soft); margin-top: 2px; }
  .contact__lines { list-style: none; margin-top: 18px; font-size: 14px; line-height: 19px; }
  .contact__label { display: inline-block; width: 22px; }

  .brand {
    position: absolute; right: 44px; top: 44px;
    display: flex; align-items: center; gap: 12px;
  }
  .brand__dot {
    width: 30px; height: 30px; border-radius: 50%;
    background: var(--brand-grey);
  }
  .brand__name {
    font-family: "Exo", Arial, sans-serif; font-weight: 500;
    font-size: 52px; line-height: 1; color: var(--brand-grey);
    letter-spacing: 1px;
  }

  .address {
    position: absolute; right: 44px; top: 178px;
    font-size: 13px; line-height: 18px; text-align: left;
  }

  .disclaimer {
    position: absolute; left: 44px; right: 44px; bottom: 22px;
    font-size: 9px; line-height: 12px; font-style: italic; color: var(--ink-soft);
  }

  /* back card */
  .wordmark {
    position: absolute; right: 46px; bottom: 42px;
    font-family: "Exo", Arial, sans-serif; font-weight: 400;
    color: var(--deboss); text-align: right;
  }
  .wordmark__name { font-size: 96px; line-height: 0.9; letter-spacing: 2px; }
  .wordmark__sub { font-size: 20px; letter-spacing: 9px; }
</style>
</head>
<body>
<main class="stage">

  <section class="card card--front" aria-label="Business card, front">
    <div class="contact">
      <p class="contact__name">Owen Marcus Hale</p>
      <p class="contact__title">Founder &amp; CEO</p>
      <ul class="contact__lines">
        <li><span class="contact__label">T</span>020 7946 0132</li>
        <li><span class="contact__label">M</span>020 7946 0132</li>
        <li><span class="contact__label">E</span>owen@rolk.com</li>
      </ul>
    </div>

    <div class="brand">
      <span class="brand__dot" aria-hidden="true"></span>
      <span class="brand__name">ROLK</span>
    </div>

    <address class="address" style="font-style:normal">
      Calder Row 14, London<br>
      United Kingdom<br>
      www.rolk.com
    </address>

    <p class="disclaimer">ROLK Investments is an Appointed Representative of Brambury Monetary Ventures Limited, which is authorised by the Pemberton Oversight Board</p>
  </section>

  <section class="card card--back" aria-label="Business card, back">
    <div class="wordmark">
      <div class="wordmark__name">ROLK</div>
      <div class="wordmark__sub">Investments</div>
    </div>
  </section>

</main>
</body>
</html>
```